Business Card Design

I am a Accredited RiverPath Officiant(r) (this title requires the Registered Trademark come after it). I am also A Non-Denominational Minister. My minister title is important, but not my primary focus. My primary line of business is custom weddings. I also offer other ceremonies across the range of life experiences. Right now the back of my card lists the other ceremonies I create and lead. I have a logo that was just developed and I want to use my logo for my cards. I have the logo in every possible format, color black/white also broken up with just the graphic of just the name. I can send other formats if needed. You can see info about my wedding work at www.lanternrites.com. My physical address is less important than my email and phone number. My secondary line of business is personalized funerals and memorials. The challenge is I don't want to have more than one card, but I want to separate weddings and funerals. Thinking funerals needs to go on the back. I hate my funeral website name(www.gentlepartingsne.com) but it might be important to use it.
Information on back of card currently says:
Specializing in Couples Centered Custom Wedding Ceremonies.
Addition Services: Creating ways to express the meaningful moments of your life, in your on way: Baby Welcoming's and Naming's, Mother/Father Parent Passages for birth and adoption, Engagement and Vow Renewals, New Home Dedications, Creative Business Ribbon Cuttings, Ceremonies of Transition-moving, home sale, business closing, career change, Croning. Ceremonies of Healing-divorce, job loss, recovery, rededication, Transgender Naming Ceremonies, Coming Out Ceremonies. Ceremonies to Celebrate life and honor death-custom funeral and personalized life memorials. Ceremony writing services also available.

Target Market(s)

95% of my business is wedding clients both gay and straight.Also do custom funerals.I also do other ceremony want to use only 1 card for all products

Industry/Entity Type

Wedding

Contact Information for Business Card

Marla J. Penwick, Non-Denominational Minister
Accredited River-Path Officiant(r)
Lantern Rites
217 Fenwick Rd. Millbrook, CT 06099
8604173926
www.lanternrites.com
tag line on front Heartfelt Custom Created Ceremonies

```html
<!DOCTYPE html>
<html lang="en">
<head>
<meta charset="utf-8">
<title>Lantern Rites – Business Card</title>
<link rel="stylesheet" href="https://fonts.googleapis.com/css2?family=Ubuntu:wght@400;500&family=Roboto+Condensed:wght@400&family=Great+Vibes&display=swap">
<style>
  :root {
    --backdrop: #ececec;
    --card: #ffffff;
    --rose: #c0392f;
    --jade: #3f9a7a;
    --ink: #2b2b2b;
    --ink-soft: #444444;
    --mist: #e9eeea;
  }
  * { box-sizing: border-box; margin: 0; padding: 0; }
  html, body { width: 1200px; height: 952px; overflow: hidden; }
  body {
    background: var(--backdrop);
    font-family: "Ubuntu", sans-serif;
    color: var(--ink);
    display: flex;
    flex-direction: column;
    align-items: center;
    justify-content: center;
    gap: 36px;
  }
  .card {
    position: relative;
    width: 735px;
    height: 420px;
    background: var(--card);
    box-shadow: 0 2px 10px rgba(0,0,0,.12);
    overflow: hidden;
  }
  .card__stripe {
    position: absolute; left: 0; right: 0; bottom: 0; height: 9px;
  }
  .card--front .card__stripe { background: var(--rose); }
  .card--back .card__stripe { background: var(--jade); }

  .card__ornament {
    position: absolute;
    right: -40px; bottom: -40px;
    width: 300px; height: 260px;
    border-radius: 50%;
    background: radial-gradient(circle at 50% 50%, rgba(192,57,47,.10), var(--mist) 45%, rgba(233,238,234,0) 72%);
  }

  /* front */
  .brand {
    position: absolute; left: 45px; top: 105px; width: 290px;
    display: flex; flex-direction: column; align-items: center;
  }
  .brand__row { display: flex; align-items: center; gap: 16px; }
  .brand__mark {
    width: 84px; height: 84px; border-radius: 50%;
    background: var(--jade);
  }
  .brand__name {
    font-size: 30px; font-weight: 400; color: var(--rose); line-height: 1.05;
  }
  .brand__tagline {
    margin-top: 22px;
    font-family: "Great Vibes", cursive;
    font-size: 25px; color: var(--jade); white-space: nowrap;
  }
  .divider {
    position: absolute; left: 370px; top: 60px; width: 2px; height: 250px;
    background: var(--jade);
  }
  .contact {
    position: absolute; right: 40px; top: 95px; text-align: right;
  }
  .contact__name { font-size: 25px; font-weight: 400; color: var(--rose); }
  .contact__title { font-size: 16px; color: var(--ink); line-height: 1.3; }
  .contact__list {
    list-style: none; margin-top: 40px;
    font-family: "Roboto Condensed", sans-serif; font-size: 16px; line-height: 1.45;
  }
  .contact__list li { display: flex; justify-content: flex-end; align-items: center; gap: 8px; }
  .contact__icon { width: 13px; height: 13px; flex: none; }
  .contact__spacer { width: 13px; flex: none; }

  /* back */
  .services {
    position: absolute; left: 42px; right: 42px; top: 62px;
    font-size: 20.5px; line-height: 1.33; text-align: justify; color: var(--ink-soft);
  }
  .services__label { color: var(--rose); }
</style>
</head>
<body>

<section class="card card--front" aria-label="Card front">
  <div class="card__ornament" role="img" aria-label="Faint swirl ornament"></div>
  <div class="brand">
    <div class="brand__row">
      <span class="brand__mark"></span>
      <span class="brand__name">Marla<br>Penwick</span>
    </div>
    <p class="brand__tagline">Heartfelt Custom Created Ceremonies</p>
  </div>
  <div class="divider"></div>
  <div class="contact">
    <h1 class="contact__name">Marla J. Penwick</h1>
    <p class="contact__title">Non-Denominational Minister</p>
    <p class="contact__title">Accredited River-Path Officiant(r)</p>
    <ul class="contact__list">
      <li>Lantern Rites<span class="contact__spacer"></span></li>
      <li>217 Fenwick Rd. Millbrook, CT 06099
        <svg class="contact__icon" viewBox="0 0 12 12" aria-hidden="true"><path d="M6 0.5a4 4 0 0 0-4 4c0 3 4 7 4 7s4-4 4-7a4 4 0 0 0-4-4z" fill="var(--rose)"/><circle cx="6" cy="4.5" r="1.5" fill="#fff"/></svg>
      </li>
      <li>8604173926
        <svg class="contact__icon" viewBox="0 0 12 12" aria-hidden="true"><path d="M2.5 1l2 2.2-1 1.3c.8 1.6 1.9 2.7 3.5 3.5l1.3-1 2.2 2-1 1.5C5.5 10.5 1.5 6.5 1 2z" fill="var(--rose)"/></svg>
      </li>
      <li>www.lanternrites.com
        <svg class="contact__icon" viewBox="0 0 12 12" aria-hidden="true"><rect x="0.5" y="2" width="11" height="8" fill="var(--rose)"/><path d="M0.5 2l5.5 4.5L11.5 2" fill="none" stroke="#fff" stroke-width="1"/></svg>
      </li>
    </ul>
  </div>
  <div class="card__stripe"></div>
</section>

<section class="card card--back" aria-label="Card back">
  <div class="card__ornament" role="img" aria-label="Faint swirl ornament"></div>
  <p class="services">
    <span class="services__label">Specializing in :</span> Couples Centered Custom Wedding Ceremonies.
    <span class="services__label">Addition Services:</span> Creating ways to express the meaningful moments of your life, in your on way: Baby Welcoming's and Naming's, Mother/Father Parent Passages for birth and adoption, Engagement and Vow Renewals, New Home Dedications, Creative Business Ribbon Cuttings, Ceremonies of Transition-moving, home sale, business closing, career change, Croning, Ceremonies of Healing-divorce, job loss, recovery, rededication, Transgender Naming Ceremonies, Coming Out Ceremonies. Ceremonies to Celebrate life and honor death-custom funeral and personalized life memorials. Ceremony writing services also available.
  </p>
  <div class="card__stripe"></div>
</section>

</body>
</html>
```